business card with 2 locations on 1 card

I need a modern looking business card that I would use at 2 different locations. Possibly 1 location on 1 side and other location on other side. One should be able to distinguish the 2 locations immediately before having to read the address or description on card. You can take a look at my website to see what I'm drawn to. The logo is brand new that I just purchased on Craft Hive. I want to emphasize family.
Updates

Let's not use the yellow and blue colors. Added Thursday, August 31, 2017

Target Market(s)

women and children

Industry/Entity Type

Health And Wellness

Contact Information for Business Card

Business name: Willow Brook Chiropractic & Acupuncture
My name: Lorin Daske
Job title: DC, MAOM, LAc (CA), CNS

Location 1
Address: 4817 Marlowe Blvd, Suite B-100, Frisco, TX 75034
Phone: (469) 555-0182
Fax: (972) 555-0137

Location 2
Address: 1936 Belvane Road, Suite 100, Plano, TX 75075
Phone: (469) 555-0169
Fax: (972) 555-0137

Email: drlorindaske@mailnest.example
Website: www.drlorindaske.example

Font styles to use
Serif
Sans Serif

Colors

Designer to choose colors to be used in the design.

Requirements
Must have
• distinction between 2 locations.
Nice to have
• Colors preference below is there. But I like to see what you come up with too!

```html
<!DOCTYPE html>
<html lang="en">
<head>
<meta charset="utf-8">
<title>Willow Brook – Business Cards</title>
<link rel="stylesheet" href="https://fonts.googleapis.com/css2?family=Cinzel&family=Questrial&display=swap">
<style>
  :root {
    --page: #e9e9e6;
    --teal: #22625a;
    --teal-deep: #2b6f78;
    --green-mid: #a8c56b;
    --green-light: #c7df8c;
    --paper: #f3f3f1;
    --ink: #3a3a3a;
    --white: #ffffff;
  }
  * { margin: 0; padding: 0; box-sizing: border-box; }
  html, body { width: 1200px; height: 874px; overflow: hidden; background: var(--page); }
  .canvas { position: relative; width: 1200px; height: 874px; }
  .card {
    position: absolute; left: 250px; width: 700px; height: 400px;
    box-shadow: 0 6px 18px rgba(0,0,0,.18); overflow: hidden;
  }
  .card--frisco { top: 27px; }
  .card--plano { top: 447px; }
  .card__bg { position: absolute; inset: 0; }
  .brand {
    position: absolute; left: 40px; top: 70px; width: 260px; text-align: center;
    color: var(--white); font-family: "Cinzel", serif;
  }
  .brand__mark {
    width: 86px; height: 86px; border-radius: 50%; border: 3px solid var(--white);
    margin: 0 auto 14px;
  }
  .brand__name { font-size: 27px; line-height: 1.1; letter-spacing: 1px; }
  .brand__sub { font-size: 12px; letter-spacing: 1px; margin-top: 4px; }
  .web {
    position: absolute; left: 50px; top: 292px; color: var(--white);
    font-family: "Questrial", sans-serif; font-size: 14px; line-height: 1.5;
  }
  .details {
    position: absolute; left: 462px; top: 78px; font-family: "Questrial", sans-serif; color: var(--ink);
  }
  .details__name { color: var(--teal); font-size: 30px; font-weight: 700; letter-spacing: .5px; }
  .details__title { font-size: 14px; margin-top: 4px; letter-spacing: .5px; }
  .details__office { color: var(--teal); font-size: 17px; font-weight: 700; margin-top: 34px; }
  .details__lines { font-size: 16px; line-height: 1.3; margin-top: 4px; }
</style>
</head>
<body>
<main class="canvas">

  <article class="card card--frisco">
    <svg class="card__bg" viewBox="0 0 700 400" width="700" height="400" aria-hidden="true">
      <rect width="700" height="400" fill="var(--teal)"/>
      <path d="M250,400 Q230,320 275,250 L300,400Z" fill="var(--teal-deep)"/>
      <path d="M340,0 Q230,170 290,400 L700,400 L700,0Z" fill="var(--green-mid)"/>
      <path d="M395,0 Q270,170 310,400 L700,400 L700,0Z" fill="var(--green-light)"/>
      <path d="M445,0 Q300,170 335,400 L700,400 L700,0Z" fill="var(--paper)"/>
    </svg>
    <div class="brand">
      <div class="brand__mark"></div>
      <div class="brand__name">Willow Brook</div>
      <div class="brand__sub">Chiropractic &amp; Acupuncture</div>
    </div>
    <div class="web">
      E: drlorindaske@mailnest.example<br>
      W: www.drlorindaske.example
    </div>
    <div class="details">
      <div class="details__name">Lorin Daske</div>
      <div class="details__title">DC, MAOM, LAc (CA), CNS</div>
      <div class="details__office">Frisco’s Office</div>
      <div class="details__lines">
        A: 4817 Marlowe Blvd,<br>
        Suite B-100,<br>
        Frisco, TX 75034<br>
        Phone: (469) 555-0182<br>
        Fax: (972) 555-0137
      </div>
    </div>
  </article>

  <article class="card card--plano">
    <svg class="card__bg" viewBox="0 0 700 400" width="700" height="400" aria-hidden="true">
      <rect width="700" height="400" fill="var(--teal)"/>
      <path d="M250,400 Q230,320 275,250 L300,400Z" fill="var(--teal-deep)"/>
      <path d="M340,0 Q230,170 290,400 L700,400 L700,0Z" fill="var(--green-mid)"/>
      <path d="M395,0 Q270,170 310,400 L700,400 L700,0Z" fill="var(--green-light)"/>
      <path d="M445,0 Q300,170 335,400 L700,400 L700,0Z" fill="var(--paper)"/>
    </svg>
    <div class="brand">
      <div class="brand__mark"></div>
      <div class="brand__name">Willow Brook</div>
      <div class="brand__sub">Chiropractic &amp; Acupuncture</div>
    </div>
    <div class="web">
      E: drlorindaske@mailnest.example<br>
      W: www.drlorindaske.example
    </div>
    <div class="details">
      <div class="details__name">Lorin Daske</div>
      <div class="details__title">DC, MAOM, LAc (CA), CNS</div>
      <div class="details__office">Plano’s Office</div>
      <div class="details__lines">
        A: 1936 Belvane Road,<br>
        Suite 100,<br>
        Plano, TX 75075<br>
        Phone: (469) 555-0169<br>
        Fax: (972) 555-0137
      </div>
    </div>
  </article>

</main>
</body>
</html>
```